依頼詳細
・リスティングでの運用を考えているので、コンバージョンを期待できるデザイン、サイト構成
・レスポンシブでコーディングするためそれを念頭に置いたデザイン
・提案デザインはスマホ、PC両画面でお願いします。
・サイト構成も変わる可能性が高いので、HTMLやCSSでの変更が容易なデザイン
(メニューなどを画像にしないetc)
・奇抜さよりも安心感
・病院関係のウェブサイト構築実績のある方歓迎
・病院の場所はみなとみらいです。
ページ数
2ページ
希望イメージ
シンプル 複雑
単色 カラフル
暗い 明るい
日常 高級
遊び心 厳粛
未来的 伝統的
女性的 男性的
希望する色
青系、水色系、緑系、黄・オレンジ系
納品ファイル
• 高解像度JPG (.jpg)
• フォトショップ形式 (.psd)
補足説明
■ 補足
--------------------------------
・基本HTMLコーディングは無しで構いませんが、
対応可能な方はコーディング作業についてもお見積ください。

・採用された方は今後も引続き作業をお願いすることになると思います。

■ 注意点

・お渡しできる素材は、サイトマップのみとなります
・病院名なども決まっていないので、ロゴなどは仮のもので構いません。
・サイトの中の文言なども仮の文章で構いません。
・写真素材も仮のもので構いません。
(最終的には素材もしくは撮影した写真に入れ替えます。)

○想定サイトマップ
診療科目
病院案内
├ ご挨拶・理念
├ 施設案内
└ ドクター紹介
アクセス
よくある質問
採用情報
サイトマップ
お問い合わせ
予約

※サイト構成も決定ではないので提案頂く形でも構いません。

参考サイト
http://www.tokuro-dental.com/
https://www.clinic-mikura.com/
ウェブサイトの構成が、内科・整形外科・歯科の診療科目を一つのサイトで集患する形に変更になりました。大きい枠組みで変わるのはこれ以降はないと思います。素敵なデザイナー様との出会いを期待しております。
お盆に入ってしまうので、締切を延長させていただきました。今後も数々の案件抱えておりますので、長いお付き合いができるデザイナー様との出会いを期待しております。
たくさんのご応募、誠にありがとうございます!

これから社内で選定を行います。
一週間以内には決定できると思いますので少々お待ち頂ければと思います。
よろしくお願いいたします。
デザインの選定に時間がかかっておりますので、決定までもう少々お待ち頂ければと思います。申し訳ありません、よろしくお願いいたします。
■ 選んだ理由

シンプルにデザインがまとまっていたところと、アイコンなどを使いぱっと見た時のわかりやすさ、写真を変更しても違和感なくマッチしそうな点などを評価させていただきました。

■ 提案者全員のお礼・コメント

この度は弊社コンペにご参加頂き誠にありがとうございます。
優れたデザイン・提案を多数頂きとても感謝しております。

ギリギリまでどの提案を採用させていただくか迷いましたが、
今回はこのような結果となりました。

またの機会がありましたら、またぜひご参加頂ければ幸いです。
ありがとうございました。

```html
<!DOCTYPE html>
<html lang="ja">
<head>
<meta charset="utf-8">
<title>病院名病院名病院名</title>
<link href="https://fonts.googleapis.com/css2?family=Noto+Sans+JP:wght@400;500;700&family=Noto+Serif+JP:wght@500;700&display=swap" rel="stylesheet">
<style>
:root{
  --teal:#46b5b8;
  --teal-dark:#2f9ea2;
  --teal-light:#e8f5f5;
  --ink:#333;
  --muted:#777;
  --line:#dcdcdc;
  --gray-bg:#f2f2f2;
  --nav-bg:#ebebeb;
}
*{box-sizing:border-box;margin:0;padding:0}
html,body{width:1200px;height:3460px;overflow:hidden}
body{font-family:"Noto Sans JP",sans-serif;color:var(--ink);background:#fff;font-size:13px;line-height:1.7;position:relative}
.wrap{width:900px;margin:0 auto;position:relative}

/* header */
.site-header{height:130px;position:relative}
.header-note{position:absolute;left:150px;top:6px;font-size:11px;color:var(--muted)}
.brand{position:absolute;left:150px;top:38px;display:flex;align-items:center;gap:12px}
.brand-mark{width:62px;height:48px;background:var(--teal);color:#fff;display:flex;align-items:center;justify-content:center;font-size:15px;font-weight:500}
.brand-name{font-family:"Noto Serif JP",serif;font-size:22px;font-weight:700;letter-spacing:1px}
.hours{position:absolute;font-size:10px;border-collapse:collapse}
.hours th,.hours td{border-bottom:1px solid var(--line);padding:3px 6px;text-align:center;font-weight:400}
.hours th.slot{text-align:left;white-space:nowrap}
.hours thead th{background:var(--teal);color:#fff}
.dot{display:inline-block;width:7px;height:7px;border-radius:50%;background:var(--teal)}
.header-hours{left:470px;top:20px}
.phones{position:absolute;left:800px;top:16px;display:flex;flex-direction:column;gap:5px}
.phone-row{display:flex;align-items:center;gap:10px}
.dept-tag{width:64px;font-size:11px;background:var(--gray-bg);border:1px solid var(--line);text-align:center;color:var(--muted)}
.phone-num{color:var(--teal);font-size:24px;font-weight:700;line-height:1;display:flex;align-items:center;gap:6px}
.header-small{position:absolute;left:800px;top:106px;font-size:10px;color:var(--muted)}

/* nav */
.global-nav{background:var(--nav-bg);height:42px}
.global-nav ul{list-style:none;display:flex;width:900px;margin:0 auto;height:100%}
.global-nav li{flex:1;text-align:center;line-height:42px;font-size:13px;border-right:1px solid #d6d6d6}
.global-nav li.active{background:var(--teal);color:#fff}

/* hero */
.hero{height:440px;background:
  linear-gradient(90deg,rgba(255,255,255,.0) 0%,rgba(255,255,255,.55) 45%,rgba(255,255,255,0) 100%),
  linear-gradient(180deg,#f6f8f7 0%,#eaf0ee 48%,#cfdcd4 60%,#bccab8 100%)}

/* philosophy */
.philosophy{height:300px;padding-top:40px}
.philosophy .wrap{display:flex;gap:24px}
.vertical-title{writing-mode:vertical-rl;font-family:"Noto Serif JP",serif;font-size:22px;font-weight:700;color:var(--teal);border-right:2px solid var(--teal);padding-right:10px;height:180px}
.philosophy p{width:340px;font-size:12px;line-height:2;color:#555}
.photo-ct{width:480px;height:210px;background:
  radial-gradient(ellipse at 55% 55%,#ffffff 0%,#eef2f5 35%,transparent 60%),
  linear-gradient(135deg,#dfe7ee,#b9c8d4)}

/* departments */
.departments{background:linear-gradient(180deg,#eef7f6,#e2f1f0);height:720px;padding-top:50px}
.section-title{text-align:center;font-size:20px;font-weight:700;letter-spacing:2px;position:relative;margin-bottom:30px}
.section-title::after{content:"";display:block;width:40px;height:3px;background:var(--teal);margin:8px auto 0}
.cards{display:flex;justify-content:space-between}
.card{width:280px;background:#fff;padding-bottom:20px;box-shadow:0 1px 3px rgba(0,0,0,.08)}
.card-head{display:flex;align-items:center;justify-content:center;gap:8px;font-size:17px;font-weight:700;color:var(--teal);background:var(--teal-light);height:40px}
.card-icon{width:26px;height:26px;border-radius:50%;background:var(--teal);display:flex;align-items:center;justify-content:center}
.card-photo{height:190px}
.card-photo.internal{background:linear-gradient(135deg,#bcd3e6,#6f93b4)}
.card-photo.ortho{background:linear-gradient(135deg,#e9ddd0,#a99480)}
.card-photo.dental{background:linear-gradient(135deg,#cfe7ec,#6fa3b0)}
.card p{font-size:11px;line-height:1.9;padding:14px 22px 10px;color:#555}
.btn-small{display:block;width:110px;margin:0 auto;background:var(--teal);color:#fff;font-size:11px;text-align:center;padding:6px 0}
.cta{display:flex;align-items:center;justify-content:center;width:700px;height:80px;margin:40px auto 0;background:var(--teal);color:#fff;font-size:20px;letter-spacing:2px;font-weight:500;box-shadow:0 3px 0 var(--teal-dark)}

/* news */
.news{height:320px;padding-top:44px}
.news-list{list-style:none;border-top:1px solid var(--line)}
.news-list li{display:flex;gap:40px;padding:12px 40px;border-bottom:1px solid var(--line);font-size:12px}
.news-date{color:var(--teal);width:90px}
.more{position:absolute;right:0;margin-top:20px;background:var(--teal);color:#fff;font-size:11px;padding:5px 20px}

/* access */
.access{height:520px;background:linear-gradient(180deg,#f3f3f3,#ebebeb);padding-top:50px}
.access .wrap{display:flex;justify-content:space-between}
.access-title{font-size:20px;font-weight:700;color:var(--teal);border-left:4px solid var(--teal);padding-left:12px;margin-bottom:20px}
.access-info{width:380px;font-size:12px;line-height:2}
.access-info .addr{margin-top:30px;color:#555}
.access-btn{display:inline-block;margin-top:50px;background:var(--teal);color:#fff;padding:8px 36px;font-size:12px}
.map{width:420px;height:420px;background:
  linear-gradient(160deg,transparent 55%,rgba(150,190,215,.55) 56%,rgba(150,190,215,.55) 75%,transparent 76%),
  linear-gradient(135deg,#eef0ea,#d9dee0)}

/* footer info */
.footer-info{height:640px;padding-top:60px}
.footer-info .wrap{display:flex;justify-content:space-between}
.footer-left{width:400px;font-size:12px}
.footer-left .brand{position:static;margin-bottom:20px}
.footer-left .addr{color:#555;line-height:1.9}
.footer-left .access-btn{margin-top:30px}
.footer-hours{position:static;font-size:11px}
.footer-times{font-size:11px;color:#555;margin-top:16px;line-height:1.9}
.footer-phones{display:flex;justify-content:space-between;margin-top:40px;padding-top:20px;border-top:1px solid var(--line)}
.footer-cta{margin-top:40px}
.pagetop{position:absolute;right:60px;top:3210px;width:58px;height:58px;background:var(--teal);display:flex;align-items:center;justify-content:center}

/* bottom */
.footer-links{background:var(--gray-bg);height:200px;padding-top:40px;text-align:center;font-size:11px;color:#555;line-height:1.9}
.copyright{height:148px;text-align:center;font-size:10px;color:var(--muted);padding-top:14px}
</style>
</head>
<body>

<header class="site-header">
  <p class="header-note">みなとみらいの内科・整形外科・歯科</p>
  <div class="brand"><span class="brand-mark">ロゴ</span><span class="brand-name">病院名病院名病院名</span></div>

  <table class="hours header-hours">
    <thead><tr><th class="slot">診療時間</th><th>月</th><th>火</th><th>水</th><th>木</th><th>金</th><th>土</th><th>日祝</th></tr></thead>
    <tbody>
      <tr><th class="slot">9:00〜13:00</th><td><span class="dot"></span></td><td><span class="dot"></span></td><td><span class="dot"></span></td><td><span class="dot"></span></td><td><span class="dot"></span></td><td><span class="dot"></span></td><td>-</td></tr>
      <tr><th class="slot">14:00〜18:00</th><td><span class="dot"></span></td><td><span class="dot"></span></td><td>-</td><td><span class="dot"></span></td><td><span class="dot"></span></td><td>-</td><td>-</td></tr>
      <tr><th class="slot">18:00〜20:00</th><td><span class="dot"></span></td><td>-</td><td><span class="dot"></span></td><td>-</td><td><span class="dot"></span></td><td>-</td><td>-</td></tr>
    </tbody>
  </table>

  <div class="phones">
    <div class="phone-row"><span class="dept-tag">内科</span><span class="phone-num"><svg width="18" height="18" viewBox="0 0 24 24"><path fill="#46b5b8" d="M6.6 10.8a15 15 0 0 0 6.6 6.6l2.2-2.2c.3-.3.7-.4 1-.2 1.1.4 2.3.6 3.6.6.6 0 1 .4 1 1V20c0 .6-.4 1-1 1A17 17 0 0 1 3 4c0-.6.4-1 1-1h3.5c.6 0 1 .4 1 1 0 1.3.2 2.5.6 3.6.1.3 0 .7-.2 1z"/></svg>03-555-0142</span></div>
    <div class="phone-row"><span class="dept-tag">整形外科</span><span class="phone-num"><svg width="18" height="18" viewBox="0 0 24 24"><path fill="#46b5b8" d="M6.6 10.8a15 15 0 0 0 6.6 6.6l2.2-2.2c.3-.3.7-.4 1-.2 1.1.4 2.3.6 3.6.6.6 0 1 .4 1 1V20c0 .6-.4 1-1 1A17 17 0 0 1 3 4c0-.6.4-1 1-1h3.5c.6 0 1 .4 1 1 0 1.3.2 2.5.6 3.6.1.3 0 .7-.2 1z"/></svg>03-555-0142</span></div>
    <div class="phone-row"><span class="dept-tag">歯科</span><span class="phone-num"><svg width="18" height="18" viewBox="0 0 24 24"><path fill="#46b5b8" d="M6.6 10.8a15 15 0 0 0 6.6 6.6l2.2-2.2c.3-.3.7-.4 1-.2 1.1.4 2.3.6 3.6.6.6 0 1 .4 1 1V20c0 .6-.4 1-1 1A17 17 0 0 1 3 4c0-.6.4-1 1-1h3.5c.6 0 1 .4 1 1 0 1.3.2 2.5.6 3.6.1.3 0 .7-.2 1z"/></svg>03-555-0142</span></div>
  </div>
  <p class="header-small">受付は診療終了の30分前までです。</p>
</header>

<nav class="global-nav">
  <ul>
    <li class="active">TOP</li><li>診療科目</li><li>病院案内</li><li>アクセス</li><li>よくある質問</li><li>採用情報</li><li>お問い合わせ</li><li>予約</li>
  </ul>
</nav>

<div class="hero" role="img" aria-label="明るい病院の待合ロビーの写真"></div>

<section class="philosophy">
  <div class="wrap">
    <h2 class="vertical-title">当院の想い</h2>
    <p>ここにテキストが入ります。ここにテキストが入ります。ここにテキストが入ります。ここにテキストが入ります。ここにテキストが入ります。ここにテキストが入ります。ここにテキストが入ります。ここにテキストが入ります。ここにテキストが入ります。ここにテキストが入ります。</p>
    <div class="photo-ct" role="img" aria-label="CT検査装置のある検査室の写真"></div>
  </div>
</section>

<section class="departments">
  <div class="wrap">
    <h2 class="section-title">診療科目</h2>
    <div class="cards">
      <article class="card">
        <h3 class="card-head"><span class="card-icon"><svg width="14" height="14" viewBox="0 0 14 14"><path d="M5 1h4v4h4v4H9v4H5V9H1V5h4z" fill="#fff"/></svg></span>内科</h3>
        <div class="card-photo internal" role="img" aria-label="内科の診察風景の写真"></div>
        <p>ここにテキストが入ります。ここにテキストが入ります。ここにテキストが入ります。ここにテキストが入ります。</p>
        <span class="btn-small">詳しくみる</span>
      </article>
      <article class="card">
        <h3 class="card-head"><span class="card-icon"><svg width="14" height="14" viewBox="0 0 14 14"><path d="M5 1h4v4h4v4H9v4H5V9H1V5h4z" fill="#fff"/></svg></span>整形外科</h3>
        <div class="card-photo ortho" role="img" aria-label="整形外科の診察風景の写真"></div>
        <p>ここにテキストが入ります。ここにテキストが入ります。ここにテキストが入ります。ここにテキストが入ります。</p>
        <span class="btn-small">詳しくみる</span>
      </article>
      <article class="card">
        <h3 class="card-head"><span class="card-icon"><svg width="14" height="14" viewBox="0 0 14 14"><path d="M5 1h4v4h4v4H9v4H5V9H1V5h4z" fill="#fff"/></svg></span>歯科</h3>
        <div class="card-photo dental" role="img" aria-label="歯科の診療風景の写真"></div>
        <p>ここにテキストが入ります。ここにテキストが入ります。ここにテキストが入ります。ここにテキストが入ります。</p>
        <span class="btn-small">詳しくみる</span>
      </article>
    </div>
    <a class="cta">ご予約はこちらから</a>
  </div>
</section>

<section class="news">
  <div class="wrap">
    <h2 class="section-title">新着情報</h2>
    <ul class="news-list">
      <li><span class="news-date">2017.08.10</span>ここにテキストが入ります。ここにテキストが入ります。ここに…</li>
      <li><span class="news-date">2017.08.10</span>ここにテキストが入ります。ここにテキストが入ります。ここに…</li>
      <li><span class="news-date">2017.08.10</span>ここにテキストが入ります。ここにテキストが入ります。ここに…</li>
    </ul>
    <span class="more">一覧を見る</span>
  </div>
</section>

<section class="access">
  <div class="wrap">
    <div class="access-info">
      <h2 class="access-title">アクセス</h2>
      <p>○○○○○内科／整形外科／歯科</p>
      <p class="addr">〒000-0000<br>○○○○県○○市○○区○○○○ 0-0-0<br>○○○○駅より徒歩0分</p>
      <span class="access-btn">詳しくみる</span>
    </div>
    <div class="map" role="img" aria-label="病院周辺の地図"></div>
  </div>
</section>

<section class="footer-info">
  <div class="wrap">
    <div class="footer-left">
      <div class="brand"><span class="brand-mark">ロゴ</span><span class="brand-name">病院名病院名病院名</span></div>
      <p class="addr">〒000-0000<br>○○○○県○○市○○区○○○○ 0-0-0</p>
      <span class="access-btn">アクセス</span>
    </div>
    <div>
      <table class="hours footer-hours">
        <thead><tr><th class="slot">診療時間</th><th>月</th><th>火</th><th>水</th><th>木</th><th>金</th><th>土</th><th>日祝</th></tr></thead>
        <tbody>
          <tr><th class="slot">9:00〜13:00</th><td><span class="dot"></span></td><td><span class="dot"></span></td><td><span class="dot"></span></td><td><span class="dot"></span></td><td><span class="dot"></span></td><td><span class="dot"></span></td><td>-</td></tr>
          <tr><th class="slot">14:00〜18:00</th><td><span class="dot"></span></td><td><span class="dot"></span></td><td>-</td><td><span class="dot"></span></td><td><span class="dot"></span></td><td>-</td><td>-</td></tr>
          <tr><th class="slot">18:00〜20:00</th><td><span class="dot"></span></td><td>-</td><td><span class="dot"></span></td><td>-</td><td><span class="dot"></span></td><td>-</td><td>-</td></tr>
        </tbody>
      </table>
      <p class="footer-times">受付時間　平日 9:00〜12:30<br>　　　　　土曜 9:00〜12:00</p>
    </div>
  </div>
  <div class="wrap footer-phones">
    <div class="phone-row"><span class="dept-tag">内科</span><span class="phone-num">03-555-0142</span></div>
    <div class="phone-row"><span class="dept-tag">整形外科</span><span class="phone-num">03-555-0142</span></div>
    <div class="phone-row"><span class="dept-tag">歯科</span><span class="phone-num">03-555-0142</span></div>
  </div>
  <div class="wrap"><a class="cta footer-cta">ご予約はこちらから</a></div>
</section>

<a class="pagetop" aria-label="ページトップへ"><svg width="30" height="20" viewBox="0 0 30 20"><path d="M3 17 15 5l12 12" fill="none" stroke="#fff" stroke-width="3"/></svg></a>

<footer>
  <div class="footer-links">
    診療科目 ｜ 病院案内 ｜ アクセス ｜ よくある質問 ｜ 採用情報 ｜ サイトマップ ｜ お問い合わせ ｜ 予約<br>
    ご挨拶・理念<br>施設案内<br>ドクター紹介
  </div>
  <p class="copyright">Copyright © 病院名病院名病院名 All Rights Reserved.</p>
</footer>

</body>
</html>
```